Brindlewood Court Apartments Business Cards

We need a business card design for a small apartment community in the metro-Detroit area. The property has a park-like feel and is surrounded by trees and ponds.

The logo colors are:
R=9 G=117 B=127
R=210 G=183 B=114

Contact Information for Business Card

Marla Finch
Property Manager
Brindlewood Court Apartments
352 Brindlewood Way
Alder Falls, OH 48190
Phone (248)517-2039

```html
<!DOCTYPE html>
<html lang="en">
<head>
<meta charset="utf-8">
<title>Brindlewood Court Apartments – Business Card</title>
<link href="https://fonts.googleapis.com/css2?family=Tinos:wght@400;700&display=swap" rel="stylesheet">
<style>
  :root {
    --bg: #cccccc;
    --card: #ffffff;
    --band: #35c0cc;
    --teal: #09757f;
    --gold: #d2b772;
    --white: #ffffff;
    --icon: #2f2f2f;
    --partner: #1f5aa0;
  }
  * { margin: 0; padding: 0; box-sizing: border-box; }
  html, body { width: 1200px; height: 1200px; overflow: hidden; }
  body {
    background: var(--bg);
    font-family: "Tinos", "Times New Roman", serif;
    position: relative;
  }
  .card {
    position: absolute;
    left: 270px; top: 70px;
    width: 660px; height: 1060px;
    background: var(--card);
    text-align: center;
  }
  .brand-art {
    position: absolute;
    left: 220px; top: 92px;
    width: 220px; height: 150px;
    border-radius: 50%;
    background: radial-gradient(circle at 55% 45%, var(--gold) 0 32%, var(--teal) 70%);
    opacity: 0.9;
  }
  .brand-name {
    position: absolute; left: 0; right: 0; top: 262px;
    color: var(--gold);
    font-weight: 700;
    font-size: 39px;
    letter-spacing: 1px;
    line-height: 1;
  }
  .brand-sub {
    position: absolute; left: 0; right: 0; top: 312px;
    color: var(--gold);
    font-weight: 700;
    font-size: 24px;
    letter-spacing: 2px;
    line-height: 1;
  }
  .band { position: absolute; left: 0; right: 0; background: var(--band); color: var(--white); }
  .band--name { top: 404px; height: 204px; }
  .band--contact { top: 666px; height: 225px; }
  .person-name {
    margin-top: 30px;
    font-weight: 700;
    font-size: 80px;
    line-height: 1;
    letter-spacing: 1px;
  }
  .person-role {
    margin-top: 22px;
    font-size: 38px;
    letter-spacing: 2px;
    line-height: 1;
  }
  .contact-icon { display: block; margin: 0 auto; width: 34px; height: 34px; }
  .contact-icon--home { margin-top: 32px; }
  .contact-icon--phone { margin-top: 20px; }
  .contact-address { margin-top: 12px; font-size: 27px; line-height: 1; }
  .contact-phone { margin-top: 12px; font-size: 24px; line-height: 1; }
  .partner {
    position: absolute; left: 0; right: 0; top: 950px;
    display: flex; align-items: center; justify-content: center; gap: 10px;
    color: var(--partner);
    font-weight: 700;
    font-size: 20px;
  }
  .partner-dot { width: 22px; height: 22px; border-radius: 50%; background: var(--partner); }
</style>
</head>
<body>
  <div class="card">
    <div class="brand-art" role="img" aria-label="Property emblem: bird in flight over a setting sun"></div>
    <div class="brand-name">BRINDLEWOOD COURT</div>
    <div class="brand-sub">APARTMENTS</div>

    <div class="band band--name">
      <div class="person-name">MARLA FINCH</div>
      <div class="person-role">PROPERTY MANAGER</div>
    </div>

    <div class="band band--contact">
      <svg class="contact-icon contact-icon--home" viewBox="0 0 24 24" aria-hidden="true">
        <circle cx="12" cy="12" r="12" fill="var(--icon)"/>
        <path d="M12 5.5 5 11.5h2v6h3.5v-4h3v4H17v-6h2z" fill="#fff"/>
      </svg>
      <div class="contact-address">352 Brindlewood Way Alder Falls, OH 48190</div>
      <svg class="contact-icon contact-icon--phone" viewBox="0 0 24 24" aria-hidden="true">
        <circle cx="12" cy="12" r="12" fill="var(--icon)"/>
        <path d="M8.6 6.5c.4-.3 1-.2 1.3.2l1.2 1.8c.3.4.2 1-.2 1.3l-.8.6c.6 1.4 1.7 2.6 3.1 3.3l.6-.8c.3-.4.9-.5 1.3-.2l1.8 1.2c.4.3.5.9.2 1.3l-.7 1c-.5.6-1.3.9-2.1.6-3.2-1.2-5.7-3.7-6.900-6.9-.3-.8 0-1.6.6-2.1z" fill="#fff"/>
      </svg>
      <div class="contact-phone">(248)517-2039</div>
    </div>

    <div class="partner">
      <span class="partner-dot"></span>
      <span class="partner-name">HARBORLINE PROPERTIES</span>
    </div>
  </div>
</body>
</html>
```